Non-Fiction Book Cover Series Concepts

I need front cover concepts for a non-fiction business book series. Just concepts at this stage to show to backers (full cover designs later).

The books are for leaders and business owners. A mature, sophisticated market, AND, bold and innovative.

The series needs to be extensible - the concepts need to be able to work across at least 40 books. I am happy with a colour theme, or contrasts, or icon theme, there is no limitation to the imagination.

The books need to look like they belong to a series and to also stand alone.

I prefer simple and bold.

Imagine the Heron trade series (https://www.heronbooks.example/series/tws/heron-trade-wisdom-series.html) - but I hate these designs (the colours don't work for me).

The imprint is MindfulVantagePress.example - the logo mark for the imprint is attached.

The books will be printed and ebooks - the printed version will be 5 inches by 8 inches form factor. They will be printed with a matt cover.

IF YOU WANT A BOOK TITLE TO TRY, use this:

Steady Momentum: Apply the R.A.V. Model to Inspire, Unlock and Sustain Talent

Thank you for your interest!

Target Market(s)

Business owners, leaders, entrepreneurs

Industry/Entity Type

Leadership

Font styles to use
Serif
Sans Serif

Requirements
Must have
• Extensible - the concept can work for many books and ALL books look part of the series
Nice to have
• I prefer simple, icons rather than photos
Should not have
• No photographic designs - icon, drawing

```html
<!DOCTYPE html>
<html lang="en">
<head>
<meta charset="utf-8">
<title>Steady Momentum — Series Cover Concepts</title>
<link href="https://fonts.googleapis.com/css2?family=Roboto+Condensed:wght@300;700&display=swap" rel="stylesheet">
<style>
  :root {
    --board-light: #f4f4f4;
    --board-dark: #c9c9c9;
    --paper: #ffffff;
    --ink: #111111;
    --imprint: #6a4ce0;
    --crowd-a: #2f6b5a;
    --crowd-b: #c8593c;
    --crowd-c: #34467a;
    --crowd-d: #d9a23a;
  }
  * { box-sizing: border-box; margin: 0; padding: 0; }
  html, body { width: 1200px; height: 1200px; overflow: hidden; }
  body {
    position: relative;
    background: radial-gradient(circle at 50% 50%, var(--board-light) 0%, var(--board-dark) 75%);
    font-family: "Roboto Condensed", "Arial Narrow", sans-serif;
    color: var(--ink);
  }
  .cover {
    position: absolute;
    width: 319px;
    height: 510px;
    background: var(--paper);
    overflow: hidden;
  }
  .cover--cluster { left: 115px; top: 76px; }
  .cover--valley  { left: 767px; top: 76px; }
  .cover--rise    { left: 230px; top: 636px; }
  .cover--corner  { left: 619px; top: 636px; }

  .imprint-bar {
    position: absolute;
    left: 20px; top: 24px;
    width: 280px;
    display: flex;
    align-items: flex-end;
    gap: 6px;
  }
  .imprint-bar__label {
    flex: 0 0 236px;
    font-size: 8px;
    font-weight: 700;
    letter-spacing: 0.2px;
    padding-bottom: 4px;
    border-bottom: 1.5px solid var(--imprint);
  }
  .imprint-bar__mark {
    display: flex; align-items: center; gap: 3px;
    font-size: 7px; font-weight: 700; color: var(--imprint);
    white-space: nowrap;
  }
  .imprint-bar__dot {
    width: 6px; height: 6px; border-radius: 50%; background: var(--imprint);
  }

  .title {
    position: absolute;
    left: 20px; top: 60px;
    width: 290px;
  }
  .title__lead {
    display: block;
    font-weight: 300;
    font-size: 25px;
    line-height: 33px;
  }
  .title__main {
    display: block;
    font-weight: 700;
    font-size: 24.5px;
    line-height: 33px;
    margin-top: 2px;
  }
  .crowd {
    position: absolute;
    left: 0; top: 0;
    width: 319px; height: 510px;
  }
</style>
</head>
<body>
  <svg width="0" height="0" style="position:absolute">
    <defs>
      <linearGradient id="crowd-tones" x1="0" y1="0" x2="1" y2="1">
        <stop offset="0" stop-color="#2f6b5a"/>
        <stop offset="0.35" stop-color="#34467a"/>
        <stop offset="0.7" stop-color="#c8593c"/>
        <stop offset="1" stop-color="#d9a23a"/>
      </linearGradient>
      <radialGradient id="crowd-sphere" cx="0.5" cy="0.5" r="0.5">
        <stop offset="0" stop-color="#34467a"/>
        <stop offset="0.6" stop-color="#2f6b5a"/>
        <stop offset="0.9" stop-color="#c8593c" stop-opacity="0.7"/>
        <stop offset="1" stop-color="#d9a23a" stop-opacity="0"/>
      </radialGradient>
    </defs>
  </svg>

  <article class="cover cover--cluster">
    <svg class="crowd" viewBox="0 0 319 510" role="img" aria-label="Round cluster of colourful tiled portrait icons of diverse business people">
      <ellipse cx="162" cy="352" rx="148" ry="152" fill="url(#crowd-sphere)"/>
    </svg>
    <div class="imprint-bar">
      <span class="imprint-bar__label">The imprint is MindfulVantagePress.example</span>
      <span class="imprint-bar__mark"><span class="imprint-bar__dot"></span>MVP</span>
    </div>
    <h1 class="title">
      <span class="title__lead">Steady Momentum:</span>
      <span class="title__main">Apply the R.A.V. Model<br>to Inspire, Unlock and<br>Sustain Talent</span>
    </h1>
  </article>

  <article class="cover cover--valley">
    <svg class="crowd" viewBox="0 0 319 510" role="img" aria-label="Valley-shaped crowd of colourful tiled portrait icons rising up both sides">
      <path d="M0,228 C30,360 90,432 160,434 C230,436 290,360 319,228 L319,510 L0,510 Z" fill="url(#crowd-tones)"/>
    </svg>
    <div class="imprint-bar">
      <span class="imprint-bar__label">The imprint is MindfulVantagePress.example</span>
      <span class="imprint-bar__mark"><span class="imprint-bar__dot"></span>MVP</span>
    </div>
    <h1 class="title">
      <span class="title__lead">Steady Momentum:</span>
      <span class="title__main">Apply the R.A.V. Model<br>to Inspire, Unlock and<br>Sustain Talent</span>
    </h1>
  </article>

  <article class="cover cover--rise">
    <svg class="crowd" viewBox="0 0 319 510" role="img" aria-label="Rising wedge of colourful tiled portrait icons climbing to the top right">
      <path d="M0,510 C150,440 250,340 319,184 L319,510 Z" fill="url(#crowd-tones)"/>
    </svg>
    <div class="imprint-bar">
      <span class="imprint-bar__label">The imprint is MindfulVantagePress.example</span>
      <span class="imprint-bar__mark"><span class="imprint-bar__dot"></span>MVP</span>
    </div>
    <h1 class="title">
      <span class="title__lead">Steady Momentum:</span>
      <span class="title__main">Apply the R.A.V. Model<br>to Inspire, Unlock and<br>Sustain Talent</span>
    </h1>
  </article>

  <article class="cover cover--corner">
    <svg class="crowd" viewBox="0 0 319 510" role="img" aria-label="Dense group of large colourful portrait icons in the lower left, scattering outward">
      <path d="M0,318 C70,300 160,315 180,360 C200,420 170,470 200,510 L0,510 Z" fill="url(#crowd-tones)"/>
    </svg>
    <div class="imprint-bar">
      <span class="imprint-bar__label">The imprint is MindfulVantagePress.example</span>
      <span class="imprint-bar__mark"><span class="imprint-bar__dot"></span>MVP</span>
    </div>
    <h1 class="title">
      <span class="title__lead">Steady Momentum:</span>
      <span class="title__main">Apply the R.A.V. Model<br>to Inspire, Unlock and<br>Sustain Talent</span>
    </h1>
  </article>
</body>
</html>
```